Building and Facilities Management brochure

Please refer to attached PDF, page by page with information about the brief.
SOPHISTICATED, BOLD, PROFESSIONAL BROCHURE to market our company in business meetings to Builders, Owners of buildings, Strata Committees etc.

The final design should portray quality, service, integrity,
Clear Communication

Attached is:
- pdf with details of basic layout options and wording and most of the information about the brief.
- Logo options to use
- Business card designs to understand what design we have previously had.
- Word document of the pdf if that helps to copy the information.

Target Market(s)

Professionals. Builders/developer, Strata Owners, and Building owners who want a high level of service and management of their building

Industry/Entity Type

It Company

Requirements
Must have
• - Logo
• - Contact details
• - Use of the colour in the design which has been specified.
• - Images/s of building/s
• - Use the phrase "Quality Service with Integrity"
Nice to have
• - as much of the wording as possible from the document which was uploaded, that will fit and work with the design
Should not have
• Excessive colour or variances as it needs to stay clear, bold and sophisticated.
• Too much on the page, clarity is key for clear communication without trying to clutter too much on the page.

```html
<!DOCTYPE html>
<html lang="en">
<head>
<meta charset="utf-8">
<title>Ridgeway Facilities Group – Brochure Cover Spread</title>
<link href="https://fonts.googleapis.com/css2?family=Montserrat:wght@400;600;700;800&family=Open+Sans:wght@400;600&display=swap" rel="stylesheet">
<style>
  :root{
    --brand-blue:#29a9e1;
    --brand-blue-light:#5cc4f0;
    --brand-blue-deep:#1b8ccb;
    --charcoal:#3b3d40;
    --charcoal-dark:#232527;
    --grey-mid:#8c8f93;
    --grey-light:#d9dbdd;
    --paper:#ffffff;
    --backdrop:#e6e7e8;
    --ink:#2f3033;
  }
  *{box-sizing:border-box;margin:0;padding:0}
  html,body{width:1200px;height:848px;overflow:hidden;background:var(--backdrop)}
  .spread{position:relative;width:1200px;height:848px;display:flex}
  .page{position:relative;width:600px;height:848px;background:var(--paper);overflow:hidden}
  .page svg.art{position:absolute;inset:0;width:600px;height:848px}

  /* inside-cover page */
  .welcome{position:absolute;left:48px;top:60px;width:504px;font-family:"Open Sans",sans-serif;color:var(--ink)}
  .welcome h2{font-family:"Montserrat",sans-serif;font-weight:700;font-size:19px;color:var(--brand-blue);margin-bottom:14px}
  .welcome p{font-size:11.5px;line-height:1.55;margin-bottom:8px}

  .wordmark{position:absolute;left:0;width:600px;text-align:center;font-family:"Montserrat",sans-serif;font-weight:800;color:var(--brand-blue)}
  .wordmark .initials{display:block;font-size:54px;letter-spacing:3px;line-height:1}
  .wordmark .full{display:block;font-size:17px;letter-spacing:2px;margin-top:4px;text-transform:uppercase}
  .wordmark-back{top:400px}
  .wordmark-front{top:58px}

  .contact{position:absolute;left:48px;top:640px;width:520px;font-family:"Montserrat",sans-serif;color:#fff}
  .contact-tag{display:inline-flex;align-items:center;background:var(--brand-blue);padding:7px 26px 7px 16px;border-radius:0 20px 20px 0;font-weight:700;font-size:20px;letter-spacing:1px;margin-bottom:16px}
  .contact ul{list-style:none}
  .contact li{display:flex;align-items:flex-start;gap:12px;font-size:15px;font-weight:600;line-height:1.35;margin-bottom:8px}
  .contact li svg{flex:none;margin-top:2px}

  /* front cover page */
  .city-photo{position:absolute;left:0;top:150px;width:600px;height:360px}
  .tagline{position:absolute;left:0;width:600px;top:560px;text-align:center;font-family:"Montserrat",sans-serif;font-weight:800;line-height:1.05}
  .tagline .line-1{display:block;color:#fff;font-size:40px;letter-spacing:2px}
  .tagline .line-2{display:block;color:var(--charcoal);font-size:40px;letter-spacing:2px}
  .tagline .line-3{display:block;color:#fff;font-size:62px;letter-spacing:3px}
  .web-band{position:absolute;left:0;width:600px;top:770px;text-align:center;font-family:"Montserrat",sans-serif;font-weight:700;font-size:17px;color:var(--ink);letter-spacing:.5px}
</style>
</head>
<body>
<main class="spread">

  <section class="page page-back">
    <svg class="art" viewBox="0 0 600 848" aria-hidden="true">
      <defs>
        <linearGradient id="darkFade" x1="0" y1="0" x2="0" y2="1">
          <stop offset="0" stop-color="#55585c"/>
          <stop offset="1" stop-color="#232527"/>
        </linearGradient>
      </defs>
      <path d="M0 560 C150 610 330 600 600 520 L600 848 L0 848 Z" fill="url(#darkFade)"/>
      <path d="M0 540 C150 598 330 590 600 500 L600 520 C330 606 150 614 0 560 Z" fill="var(--brand-blue)"/>
      <path d="M0 575 C160 628 340 620 600 545" fill="none" stroke="#fff" stroke-width="6"/>
      <line x1="560" y1="848" x2="600" y2="560" stroke="var(--brand-blue)" stroke-width="3"/>
    </svg>

    <div class="welcome">
      <h2>Welcome to RFG (Ridgeway Facilities Group) :</h2>
      <p>RFG provides Building and Facilities Management services to Residential and Commercial properties throughout the Greater Halden and Westmere Coast regions.</p>
      <p>With the understanding that each property has different needs and requirements, our focus is to work with clients to tailor solutions best suited for their specific requirements. Our aim is to ensure the building and facilities are managed to the highest standards while meeting the desires and goals of the owners.</p>
      <p>RFG can also provide a number of other property services, please contact us to discuss your needs and request an obligation-free proposal.</p>
    </div>

    <div class="wordmark wordmark-back">
      <span class="initials">RFG</span>
      <span class="full">Ridgeway Facilities Group</span>
    </div>

    <div class="contact">
      <div class="contact-tag">CONTACT US:</div>
      <ul>
        <li><svg width="16" height="12" viewBox="0 0 16 12"><rect x="0.5" y="0.5" width="15" height="11" rx="1" fill="none" stroke="var(--brand-blue)"/><path d="M1 1 L8 7 L15 1" fill="none" stroke="var(--brand-blue)"/></svg>hello@ridgewayfg.net</li>
        <li><svg width="16" height="20" viewBox="0 0 16 20"><path d="M8 0 C3.6 0 0 3.4 0 7.8 C0 13 8 20 8 20 C8 20 16 13 16 7.8 C16 3.4 12.4 0 8 0 Z" fill="var(--brand-blue)"/><circle cx="8" cy="7.5" r="3" fill="#fff"/></svg>Greater Halden and surrounding districts through to the<br>Westmere Coast</li>
        <li><svg width="16" height="16" viewBox="0 0 16 16"><circle cx="8" cy="8" r="7.2" fill="none" stroke="var(--brand-blue)" stroke-width="1.4"/><ellipse cx="8" cy="8" rx="3" ry="7.2" fill="none" stroke="var(--brand-blue)" stroke-width="1.2"/><line x1="1" y1="8" x2="15" y2="8" stroke="var(--brand-blue)" stroke-width="1.2"/></svg>www.ridgewayfg.net</li>
      </ul>
    </div>
  </section>

  <section class="page page-front">
    <svg class="art" viewBox="0 0 600 848" aria-hidden="true">
      <defs>
        <linearGradient id="domeBlue" x1="0" y1="0" x2="0" y2="1">
          <stop offset="0" stop-color="var(--brand-blue-light)"/>
          <stop offset="1" stop-color="var(--brand-blue-deep)"/>
        </linearGradient>
        <linearGradient id="greyBase" x1="0" y1="0" x2="0" y2="1">
          <stop offset="0" stop-color="#c9cbcd"/>
          <stop offset="1" stop-color="#8c8f93"/>
        </linearGradient>
      </defs>
      <rect x="0" y="500" width="600" height="348" fill="#eef0f1"/>
      <path d="M0 520 C180 470 420 440 600 470 L600 848 L0 848 Z" fill="var(--grey-mid)"/>
      <path d="M0 540 C180 490 420 462 600 492 L600 760 L0 760 Z" fill="url(#domeBlue)"/>
      <path d="M40 848 C50 700 110 590 220 520" fill="none" stroke="#fff" stroke-width="2"/>
      <rect x="0" y="752" width="600" height="50" fill="#fff"/>
      <rect x="0" y="802" width="600" height="46" fill="url(#greyBase)"/>
    </svg>

    <div class="wordmark wordmark-front">
      <span class="initials">RFG</span>
      <span class="full">Ridgeway Facilities Group</span>
    </div>

    <svg class="city-photo" viewBox="0 0 600 360" role="img" aria-label="Photograph of a city skyline with high-rise towers, a riverfront and a green park">
      <defs>
        <linearGradient id="cityTone" x1="0" y1="0" x2="0" y2="1">
          <stop offset="0" stop-color="#dfe8ee"/>
          <stop offset="0.45" stop-color="#9aa7b0"/>
          <stop offset="0.75" stop-color="#8a6f62"/>
          <stop offset="1" stop-color="#4f7a45"/>
        </linearGradient>
      </defs>
      <path d="M0 0 H600 V300 C420 290 200 330 0 370 Z" fill="url(#cityTone)"/>
    </svg>

    <h1 class="tagline">
      <span class="line-1">QUALITY</span>
      <span class="line-2">SERVICE WITH</span>
      <span class="line-3">INTEGRITY</span>
    </h1>

    <div class="web-band">www.ridgewayfg.net</div>
  </section>

</main>
</body>
</html>
```